Business Card Design Project

QPR Management Consulting, LLC is a management consulting firm focused on improving an organization’s health and wellness while enhancing company performance with an emphasis on winning in the marketplace, profitable growth, team building, culture enablement and innovation.

Industry/Entity Type

Business

```html
<!DOCTYPE html>
<html lang="en">
<head>
<meta charset="utf-8">
<title>QPR Management Consulting – Business Card</title>
<link href="https://fonts.googleapis.com/css2?family=Poppins:wght@400;500;600;700&display=swap" rel="stylesheet">
<style>
  :root {
    --bg: #c4f5dc;
    --card: #1a1c1d;
    --accent: #7cfc1c;
    --ink: #101010;
    --white: #ffffff;
  }
  * { margin: 0; padding: 0; box-sizing: border-box; }
  html, body { width: 1200px; height: 1000px; overflow: hidden; }
  body {
    background: var(--bg);
    font-family: "Poppins", sans-serif;
    position: relative;
  }
  .card {
    position: absolute;
    left: 250px;
    width: 700px;
    height: 400px;
    background: var(--card);
    border-radius: 40px;
    overflow: hidden;
  }
  .card--front { top: 70px; }
  .card--back { top: 530px; }

  .holder { position: absolute; left: 62px; top: 232px; }
  .holder__name {
    color: var(--accent);
    font-weight: 700;
    font-size: 34px;
    letter-spacing: 0.5px;
    line-height: 1.1;
  }
  .holder__role {
    color: var(--white);
    font-weight: 500;
    font-size: 22px;
    line-height: 1.3;
  }

  .contact-band {
    position: absolute;
    right: 0;
    background: var(--accent);
    display: flex;
    align-items: center;
    gap: 14px;
    padding: 0 16px 0 8px;
    color: var(--ink);
    font-weight: 500;
    font-size: 18px;
    line-height: 1.25;
    white-space: nowrap;
  }
  .contact-band--phone { left: 300px; top: 52px; height: 78px; font-weight: 600; }
  .contact-band--mail { left: 332px; top: 148px; height: 74px; }
  .contact-band--address { left: 364px; top: 240px; height: 74px; }
  .contact-band__icon {
    flex: none;
    width: 50px;
    height: 50px;
    border: 2px solid var(--ink);
    display: flex;
    align-items: center;
    justify-content: center;
  }
  .contact-band__icon svg { width: 32px; height: 32px; }

  .back-rule {
    position: absolute;
    left: 470px;
    right: 0;
    top: 70px;
    height: 3px;
    background: var(--accent);
  }
  .firm {
    position: absolute;
    left: 62px;
    top: 190px;
    color: var(--white);
    font-weight: 400;
    font-size: 26px;
  }
</style>
</head>
<body>
  <section class="card card--front" aria-label="Business card front">
    <div class="holder">
      <p class="holder__name">DANIEL REYES</p>
      <p class="holder__role">Creative Director</p>
    </div>

    <div class="contact-band contact-band--phone">
      <span class="contact-band__icon">
        <svg viewBox="0 0 34 34" fill="none" stroke="#101010" stroke-width="2.4"><rect x="10" y="3" width="14" height="28" rx="3"/><line x1="15" y1="26" x2="19" y2="26"/></svg>
      </span>
      <span>712 4406 391<br>836 5710 264</span>
    </div>

    <div class="contact-band contact-band--mail">
      <span class="contact-band__icon">
        <svg viewBox="0 0 34 34" fill="none" stroke="#101010" stroke-width="2.4"><rect x="3" y="8" width="28" height="19"/><polyline points="3,8 17,19 31,8"/></svg>
      </span>
      <span>daniel@qprmanagement.co.in<br>www.qprmanagement.com</span>
    </div>

    <div class="contact-band contact-band--address">
      <span class="contact-band__icon">
        <svg viewBox="0 0 34 34" fill="none" stroke="#101010" stroke-width="2.6"><polyline points="4,17 17,4 30,17"/><polyline points="10,13 10,30 24,30 24,13"/></svg>
      </span>
      <span>218, 6th Floor, KL Road,<br>NY-305417</span>
    </div>
  </section>

  <section class="card card--back" aria-label="Business card back">
    <div class="back-rule"></div>
    <p class="firm">QPR Management Consulting, LLC</p>
  </section>
</body>
</html>
```